Banner Pop Up Opt In Form REDESIGNS - SLEEK BLACK LOOK

Please redesign banners attached.

I am looking for a very sleek look....I do not like this collage of images on these current designs. Please keep all content same but use images that pop.

I have an acccount at www.pixmorrow-example.com or you can use your own images.

I like black background for somereason because it looks very sleek....but these designs should pop , build trust and credibility and have easy opt in form....SLEEK AND MODERN LOOK is what im looking for....

Target Market(s)

Consumers on websites

Requirements
Must have
• Please redesign banners attached.

Nice to have

Should not have

```html
<!DOCTYPE html>
<html lang="en">
<head>
<meta charset="utf-8">
<title>Newsletter Opt-In Banners</title>
<link href="https://fonts.googleapis.com/css2?family=Montserrat:wght@400;500;800;900&display=swap" rel="stylesheet">
<style>
  :root {
    --canvas: #c8c9cb;
    --ink: #ffffff;
    --field: #ffffff;
    --placeholder: #8a8a8a;
    --teal: #8fcfcb;
    --orange: #f6941e;
    --sand: #c49a6c;
    --green: #4a8a70;
    --red: #c8202f;
    --navy: #3a5aa8;
    --peach: #f4b08a;
  }
  * { margin: 0; padding: 0; box-sizing: border-box; }
  html, body { width: 1200px; height: 279px; overflow: hidden; }
  body { background: var(--canvas); font-family: "Montserrat", sans-serif; position: relative; }

  .banner { position: absolute; top: 28px; width: 219px; height: 219px; overflow: hidden; background: #000; color: var(--ink); }
  .banner--resort { left: 23px; }
  .banner--dining { left: 258px; }
  .banner--hotel  { left: 491px; }
  .banner--watch  { left: 725px; }
  .banner--vegas  { left: 959px; }

  .banner__photo { position: absolute; inset: 0; }
  .banner--resort .banner__photo { background: linear-gradient(160deg, #000 30%, #3a2a30 55%, #6b4c55 75%, #1c3038 100%); }
  .banner--dining .banner__photo { background: radial-gradient(circle at 80% 55%, #5a3a1c 0%, #24150a 45%, #000 80%); }
  .banner--hotel  .banner__photo { background: linear-gradient(100deg, #000 35%, #3b2a1c 65%, #6b5036 85%, #2a2522 100%); }
  .banner--watch  .banner__photo { background: linear-gradient(100deg, #000 30%, #4a4432 60%, #b5a27a 80%, #6a4a34 100%); }
  .banner--vegas  .banner__photo { background: linear-gradient(120deg, #0a0f30 30%, #1d3a8a 60%, #e8e2d0 78%, #c44a2a 90%, #1a2a6a 100%); }

  .banner__content { position: absolute; inset: 0; padding: 30px 0 0 10px; }
  .banner__headline { font-weight: 900; font-size: 15.6px; letter-spacing: -0.3px; line-height: 1; white-space: nowrap; }
  .banner__lead { font-weight: 500; font-size: 5px; margin-top: 4px; white-space: nowrap; }
  .banner__offer { font-weight: 800; font-size: 11px; line-height: 1; margin-top: 6px; text-transform: uppercase; }

  .banner--resort .banner__headline { color: var(--teal); }
  .banner--resort .banner__offer { color: var(--peach); }
  .banner--dining .banner__headline { color: var(--orange); }
  .banner--dining .banner__offer { color: var(--sand); }
  .banner--hotel  .banner__headline, .banner--hotel .banner__offer { color: var(--sand); }
  .banner--watch  .banner__headline { color: var(--green); }
  .banner--watch  .banner__offer { color: var(--ink); }
  .banner--vegas  .banner__headline { color: var(--red); }
  .banner--vegas  .banner__offer { color: var(--navy); }

  .optin { position: absolute; left: 12px; top: 94px; width: 115px; }
  .optin__field, .optin__submit { display: block; width: 115px; height: 15px; border-radius: 8px; border: 0; margin-bottom: 5px; font-family: inherit; }
  .optin__field { background: var(--field); color: var(--placeholder); font-size: 4.6px; padding-left: 5px; line-height: 15px; }
  .optin__submit { color: #fff; font-size: 4.6px; font-weight: 500; letter-spacing: 0.3px; text-align: center; line-height: 15px; }
  .banner--resort .optin__submit { background: var(--teal); color: #1b2a2a; }
  .banner--dining .optin__submit { background: var(--orange); color: #1c1206; }
  .banner--hotel  .optin__submit { background: var(--sand); color: #1c140a; }
  .banner--watch  .optin__submit { background: var(--green); }
  .banner--vegas  .optin__submit { background: var(--red); }

  .banner__note { position: absolute; left: 8px; top: 180px; width: 118px; text-align: center; font-size: 3.7px; line-height: 1.25; }
</style>
</head>
<body>

<section class="banner banner--resort">
  <div class="banner__photo" role="img" aria-label="Tropical resort pool with palm trees at sunset"></div>
  <div class="banner__content">
    <h2 class="banner__headline">WANT A GREAT OFFER!</h2>
    <p class="banner__lead">SUBSCRIBE TO OUR NEWSLETTER AND RECEIVE A COMPLIMENTARY</p>
    <p class="banner__offer">7 Night Resort/Condo<br>3500 + Locations</p>
  </div>
  <div class="optin"><span class="optin__field">Name</span><span class="optin__field">Email</span><span class="optin__field">Phone</span><span class="optin__submit">SUBMIT</span></div>
  <p class="banner__note">We will send an email and a text message with the offer<br>and instruction on how to redeem.</p>
</section>

<section class="banner banner--dining">
  <div class="banner__photo" role="img" aria-label="Candlelit restaurant table with wine glasses"></div>
  <div class="banner__content">
    <h2 class="banner__headline">WANT A GREAT OFFER!</h2>
    <p class="banner__lead">SUBSCRIBE TO OUR NEWSLETTER AND RECEIVE A COMPLIMENTARY</p>
    <p class="banner__offer">$300 Restaurant<br>Certificate</p>
  </div>
  <div class="optin"><span class="optin__field">Name</span><span class="optin__field">Email</span><span class="optin__field">Phone</span><span class="optin__submit">SUBMIT</span></div>
  <p class="banner__note">We will send an email and a text message with the offer<br>and instruction on how to redeem.</p>
</section>

<section class="banner banner--hotel">
  <div class="banner__photo" role="img" aria-label="Luxury hotel lobby lounge with armchairs"></div>
  <div class="banner__content">
    <h2 class="banner__headline">WANT A GREAT OFFER!</h2>
    <p class="banner__lead">SUBSCRIBE TO OUR NEWSLETTER AND RECEIVE A COMPLIMENTARY</p>
    <p class="banner__offer">$500 Hotel Savings<br>Card</p>
  </div>
  <div class="optin"><span class="optin__field">Name</span><span class="optin__field">Email</span><span class="optin__field">Phone</span><span class="optin__submit">SUBMIT</span></div>
  <p class="banner__note">We will send an email and a text message with the offer<br>and instruction on how to redeem.</p>
</section>

<section class="banner banner--watch">
  <div class="banner__photo" role="img" aria-label="Hand holding a smart fitness watch showing heart rate"></div>
  <div class="banner__content">
    <h2 class="banner__headline">WANT A GREAT OFFER!</h2>
    <p class="banner__lead">SUBSCRIBE TO OUR NEWSLETTER AND RECEIVE A COMPLIMENTARY</p>
    <p class="banner__offer">Smart Fitness Watch</p>
  </div>
  <div class="optin"><span class="optin__field">Name</span><span class="optin__field">Email</span><span class="optin__field">Phone</span><span class="optin__submit">SUBMIT</span></div>
  <p class="banner__note">We will send an email and a text message with the offer<br>and instruction on how to redeem.</p>
</section>

<section class="banner banner--vegas">
  <div class="banner__photo" role="img" aria-label="Las Vegas welcome sign against a dusk sky"></div>
  <div class="banner__content">
    <h2 class="banner__headline">WANT A GREAT OFFER!</h2>
    <p class="banner__lead">SUBSCRIBE TO OUR NEWSLETTER AND RECEIVE A COMPLIMENTARY</p>
    <p class="banner__offer">1-4 Night Las Vegas<br>Hotel &amp; Casino</p>
  </div>
  <div class="optin"><span class="optin__field">Name</span><span class="optin__field">Email</span><span class="optin__field">Phone</span><span class="optin__submit">SUBMIT</span></div>
  <p class="banner__note">We will send an email and a text message with the offer<br>and instruction on how to redeem.</p>
</section>

</body>
</html>
```